Local fast-growing company in the service sector

We are looking for a modern business card design, which should also appear on our letterheads

Target Market(s)

Private and industrial sectors

Contact Information for Business Card

Vorname Name
Lindkofer Str. 18
71468 Waiblingen
Tel.: 07163-418259-0
Name@kovaltec-pbz.de

Colors
9d9d9d
919191
aaaaaa

Requirements
Must have
• The logo (file) in silver

```html
<!DOCTYPE html>
<html lang="de">
<head>
<meta charset="utf-8">
<title>Visitenkarte – Kovaltec</title>
<link rel="stylesheet" href="https://fonts.googleapis.com/css2?family=Roboto:wght@400;500;700&display=swap">
<style>
  :root {
    --stage: #e6e6e6;
    --card-white: #ffffff;
    --silver-light: #f4f4f4;
    --silver-mid: #c9c9c9;
    --silver-dark: #9d9d9d;
    --logo-grey: #aaaaaa;
    --text-grey: #5e5e5e;
    --icon-grey: #919191;
    --rule: #6a6a6a;
  }
  * { margin: 0; padding: 0; box-sizing: border-box; }
  html, body {
    width: 1200px; height: 900px; overflow: hidden;
    background: var(--stage);
    font-family: "Roboto", Arial, sans-serif;
  }
  .stage {
    position: relative; width: 1200px; height: 900px;
  }
  .card {
    position: absolute; left: 320px;
    width: 560px; height: 320px;
    border-radius: 22px;
    box-shadow: 0 6px 18px rgba(0,0,0,0.18);
    overflow: hidden;
  }
  .card--back {
    top: 100px;
    background: linear-gradient(160deg, var(--silver-mid) 0%, var(--silver-light) 35%, #ffffff 50%, var(--silver-mid) 80%, var(--silver-dark) 100%);
  }
  .card--front {
    top: 480px;
    background: var(--card-white);
  }
  .brand {
    position: absolute;
    display: flex; align-items: center; gap: 12px;
    color: var(--logo-grey);
    font-weight: 700;
    letter-spacing: 1px;
  }
  .brand__mark {
    width: 34px; height: 34px; background: var(--logo-grey);
  }
  .card--back .brand {
    left: 50%; top: 50%; transform: translate(-50%, -50%);
    font-size: 44px;
  }
  .card--front .brand {
    right: 44px; top: 100px; font-size: 36px;
  }
  .card--front .brand__mark { width: 28px; height: 28px; }
  .holder-name {
    position: absolute; left: 40px; top: 38px;
    font-size: 21px; font-weight: 700; color: var(--text-grey);
  }
  .divider {
    position: absolute; left: 40px; right: 40px; top: 176px;
    height: 1px; background: var(--rule);
  }
  .contact {
    position: absolute; left: 40px; top: 190px;
    list-style: none; font-size: 15px; color: var(--text-grey);
  }
  .contact li { display: flex; align-items: center; gap: 8px; line-height: 22px; }
  .contact svg { width: 14px; height: 14px; fill: var(--icon-grey); }
  .address {
    position: absolute; right: 40px; bottom: 36px;
    font-style: normal; text-align: right;
    font-size: 16px; line-height: 22px; color: var(--text-grey);
  }
</style>
</head>
<body>
<main class="stage">
  <section class="card card--back" aria-label="Rückseite der Visitenkarte">
    <div class="brand"><span class="brand__mark"></span>KOVALTEC</div>
  </section>

  <section class="card card--front" aria-label="Vorderseite der Visitenkarte">
    <h1 class="holder-name">Vorname Name</h1>
    <div class="brand"><span class="brand__mark"></span>KOVALTEC</div>
    <div class="divider"></div>
    <ul class="contact">
      <li>
        <svg viewBox="0 0 16 16" aria-hidden="true"><rect width="16" height="16" rx="3"/><path d="M5 3.5l1.6 2.2-1 1.2c.6 1.3 1.6 2.3 2.9 2.9l1.2-1 2.2 1.6-.8 1.8C7.5 12 4 8.5 3.9 4.3z" fill="#fff"/></svg>
        07163-418259-0
      </li>
      <li>
        <svg viewBox="0 0 16 16" aria-hidden="true"><rect width="16" height="16" rx="3"/><path d="M3 5h10v6H3z M3 5l5 3.5L13 5" fill="none" stroke="#fff" stroke-width="1.2"/></svg>
        Name@kovaltec-pbz.de
      </li>
    </ul>
    <address class="address">
      Lindkofer Str. 18<br>
      71468 Waiblingen
    </address>
  </section>
</main>
</body>
</html>
```